Business Card - Double Sided

Please submit your designs.

At least one design should be similar to my sample attached:

Above the line:
1) New top left logo: Brivora (attached)
top right "TKRV" logo stays the same
2) Name: Marcus Obi, J.D.
3) Title (line 2): Regional Sales Manager
4) Subtitle (line 3): TKRV #2719, Security & R/S

Below the line:
1) Brivora, Inc. / www.brivora-inc.example
2) Address: 418 Larkmoor Lane, Ashgrove Falls, CA 95512
3) e: marcus.obi@brivora-inc.example / p: (555) 014-7391

Note: More "brivora" logos can be found with a google image search.

Target Market(s)

I sell to Fortune 1000 companies

Industry/Entity Type

Business

Colors
f37022

Requirements
Must have
• TKRV Logo

```html
<!DOCTYPE html>
<html lang="en">
<head>
<meta charset="utf-8">
<title>Brivora Business Card – Front Options</title>
<link rel="stylesheet" href="https://fonts.googleapis.com/css2?family=Didact+Gothic&family=Lato:wght@300;400;700&display=swap">
<style>
  :root {
    --brand-orange: #f37022;
    --board-orange: #f26a15;
    --stage: #2c2c2c;
    --card-white: #ffffff;
    --card-cream: #fbf9f0;
    --ink: #3a3a3a;
    --ink-soft: #666666;
  }
  * { margin: 0; padding: 0; box-sizing: border-box; }
  html, body { width: 1200px; height: 1000px; overflow: hidden; }
  body {
    position: relative;
    background: var(--board-orange);
    font-family: "Didact Gothic", "Century Gothic", sans-serif;
    color: var(--ink);
  }

  .preview {
    position: absolute;
    width: 583px;
    height: 436px;
    background: var(--stage);
  }
  .preview--classic { left: 5px; top: 2px; }
  .preview--block   { left: 612px; top: 228px; width: 588px; height: 434px; }
  .preview--rule    { left: 5px; top: 560px; height: 436px; }

  .preview__label {
    position: absolute;
    top: 0; right: 0;
    background: var(--board-orange);
    color: #fff;
    font-family: "Lato", sans-serif;
    font-weight: 300;
    font-size: 17px;
    letter-spacing: 1px;
    padding: 7px 8px 6px 6px;
  }

  .card {
    position: absolute;
    width: 460px;
    height: 262px;
    left: 62px;
    top: 88px;
    background: var(--card-white);
    overflow: hidden;
    box-shadow: 0 10px 24px rgba(0,0,0,0.45);
  }

  .brand {
    position: absolute;
    left: 22px; top: 28px;
    display: flex; align-items: center; gap: 6px;
    font-size: 18px;
    color: var(--ink);
  }
  .brand__dot {
    width: 20px; height: 20px;
    border-radius: 50%;
    background: var(--ink);
  }
  .badge {
    position: absolute;
    right: 16px; top: 12px;
    width: 28px; height: 28px;
  }

  .holder__name {
    color: var(--brand-orange);
    font-size: 24px;
    letter-spacing: 2.5px;
    white-space: nowrap;
  }
  .holder__name strong { font-weight: 700; -webkit-text-stroke: 0.6px var(--brand-orange); }
  .holder__role { font-size: 15px; color: var(--ink-soft); letter-spacing: 0.6px; line-height: 1.15; }

  .contact { font-size: 13px; line-height: 1.45; white-space: nowrap; }
  .contact b { font-weight: 700; }

  /* Option 1 — orange base band */
  .card--classic .holder { position: absolute; left: 40px; top: 80px; }
  .card--classic .band {
    position: absolute; left: 0; right: 0; top: 156px; bottom: 0;
    background: var(--brand-orange);
  }
  .card--classic .contact {
    position: absolute; right: 18px; top: 20px;
    color: #fff; text-align: right; font-size: 13.5px;
  }

  /* Option 2 — orange block on cream */
  .card--block { left: 64px; top: 86px; background: var(--card-cream); font-family: "Lato", sans-serif; }
  .card--block .brand { top: 42px; font-family: "Lato", sans-serif; }
  .card--block .block {
    position: absolute; left: 210px; top: 0;
    width: 172px; height: 142px;
    background: var(--brand-orange);
    border-radius: 0 0 10px 10px;
    color: #fff;
    padding: 76px 0 0 18px;
  }
  .card--block .holder__name { color: #fff; font-size: 15px; letter-spacing: 1px; }
  .card--block .holder__name strong { -webkit-text-stroke: 0; }
  .card--block .holder__role { color: #fff; font-size: 10.5px; letter-spacing: 0.3px; line-height: 1.35; }
  .card--block .contact {
    position: absolute; right: 16px; top: 156px;
    text-align: right; font-size: 10.5px; line-height: 1.75; color: var(--ink);
  }
  .card--block .contact b { color: var(--brand-orange); }
  .card--block .stripe {
    position: absolute; left: 0; right: 0; bottom: 10px; height: 8px;
    background: var(--brand-orange);
  }

  /* Option 3 — right-aligned with rule */
  .card--rule .holder { position: absolute; right: 40px; top: 68px; text-align: right; }
  .card--rule .holder__name { font-size: 22px; }
  .card--rule .holder__role { font-size: 14px; }
  .card--rule .rule {
    position: absolute; left: 42px; right: 0; top: 148px; height: 2px;
    background: var(--brand-orange);
  }
  .card--rule .contact {
    position: absolute; right: 30px; top: 166px;
    text-align: right; font-size: 13.5px; color: var(--ink);
  }
  .card--rule .contact b { color: var(--brand-orange); }
</style>
</head>
<body>

  <section class="preview preview--classic">
    <span class="preview__label">FRONT PREVIEW</span>
    <article class="card card--classic">
      <div class="brand"><span class="brand__dot"></span>Brivora</div>
      <svg class="badge" viewBox="0 0 28 28" aria-label="TKRV certification badge" role="img">
        <circle cx="14" cy="14" r="12" fill="none" stroke="#3a3a3a" stroke-width="2"/>
      </svg>
      <div class="holder">
        <p class="holder__name">MARCUS <strong>OBI, J.D.</strong></p>
        <p class="holder__role">Regional Sales Manager</p>
        <p class="holder__role">TKRV #2719, Security &amp; R/S</p>
      </div>
      <div class="band">
        <div class="contact">
          <p>Brivora, Inc. / <b>Website:</b> www.brivora-inc.example</p>
          <p><b>Address:</b> 418 Larkmoor Lane, Ashgrove Falls, CA 95512</p>
          <p><b>Email:</b> marcus.obi@brivora-inc.example / <b>Phone:</b> (555) 014-7391</p>
        </div>
      </div>
    </article>
  </section>

  <section class="preview preview--block">
    <span class="preview__label">FRONT PREVIEW</span>
    <article class="card card--block">
      <div class="brand"><span class="brand__dot"></span>Brivora</div>
      <svg class="badge" viewBox="0 0 28 28" aria-label="TKRV certification badge" role="img">
        <circle cx="14" cy="14" r="12" fill="none" stroke="#3a3a3a" stroke-width="2"/>
      </svg>
      <div class="block">
        <p class="holder__name">MARCUS <strong>OBI, J.D.</strong></p>
        <p class="holder__role">Regional Sales Manager</p>
        <p class="holder__role">TKRV #2719, Security &amp; R/S</p>
      </div>
      <div class="contact">
        <p>Brivora, Inc. / <b>Website:</b> www.brivora-inc.example</p>
        <p><b>Address:</b> 418 Larkmoor Lane, Ashgrove Falls, CA 95512</p>
        <p><b>Email:</b> marcus.obi@brivora-inc.example / <b>Phone:</b> (555) 014-7391</p>
      </div>
      <div class="stripe"></div>
    </article>
  </section>

  <section class="preview preview--rule">
    <span class="preview__label">FRONT PREVIEW</span>
    <article class="card card--rule">
      <div class="brand"><span class="brand__dot"></span>Brivora</div>
      <svg class="badge" viewBox="0 0 28 28" aria-label="TKRV certification badge" role="img">
        <circle cx="14" cy="14" r="12" fill="none" stroke="#3a3a3a" stroke-width="2"/>
      </svg>
      <div class="holder">
        <p class="holder__name">MARCUS <strong>OBI, J.D.</strong></p>
        <p class="holder__role">Regional Sales Manager</p>
        <p class="holder__role">TKRV #2719, Security &amp; R/S</p>
      </div>
      <div class="rule"></div>
      <div class="contact">
        <p>Brivora, Inc. / <b>Website</b>: www.brivora-inc.example</p>
        <p><b>Address</b>: 418 Larkmoor Lane, Ashgrove Falls, CA 95512</p>
        <p><b>Email</b>: marcus.obi@brivora-inc.example / <b>Phone</b>: (555) 014-7391</p>
      </div>
    </article>
  </section>

</body>
</html>
```